Control panel UI redesign for a learning simulation

Hello. I'm producing a learning simulation and need help with designing a control panel. You will see the panel on the bottom of the image. The look, colors, size, placement, etc. can change, but it has to remain horizontal, that's my only requirement. Overall, I'm open to suggestions. Thank you for your help!

NOTE: the last two items (success rate and progress) are indicators, not buttons, so they should look different from the buttons.

Industry/Entity Type

Learning

Other font styles liked:
• Open Sans

```html
<!DOCTYPE html>
<html lang="en">
<head>
<meta charset="utf-8">
<title>Learning Simulation – Control Panel</title>
<link href="https://fonts.googleapis.com/css2?family=Open+Sans:wght@400;600;700&display=swap" rel="stylesheet">
<style>
  :root {
    --studio-light: #e9ecea;
    --studio-mid: #b9c9c3;
    --studio-deep: #8fa6a0;
    --floor-warm: #e7c98f;
    --screen-frame: #f4f6f5;
    --screen-olive: #8a8a3a;
    --screen-glow: #d9d2b0;
    --presenter-tone: #9fb3cf;
    --presenter-dark: #3b3f45;
    --panel-bg: rgba(52, 56, 58, 0.94);
    --tile-teal: #1f5e56;
    --tile-border: #d7e0dd;
    --icon-disc: #ffffff;
    --label: #ffffff;
    --meter-track: rgba(255, 255, 255, 0.22);
    --meter-fill: #7fd1c2;
    --star-gold: #f2c14e;
    --nav-bg: #111314;
  }
  * { box-sizing: border-box; margin: 0; padding: 0; }
  html, body { width: 1200px; height: 675px; overflow: hidden; }
  body {
    position: relative;
    font-family: "Open Sans", Arial, sans-serif;
    background: var(--studio-light);
  }
  .studio-backdrop {
    position: absolute; inset: 0;
    background:
      linear-gradient(180deg, transparent 72%, var(--floor-warm) 80%, #f1ece2 86%, #dfe5e3 100%),
      radial-gradient(ellipse at 50% 40%, #d4dfdb 0%, var(--studio-mid) 55%, var(--studio-deep) 100%);
  }
  .studio-backdrop::before {
    content: ""; position: absolute; left: 0; right: 0; top: 0; height: 60px;
    background: linear-gradient(180deg, #f2f3f2, #dcdfdd);
  }
  .studio-backdrop::after {
    content: ""; position: absolute; left: 35px; right: 60px; top: 405px; height: 22px;
    background: #1d2326;
  }
  .world-screen {
    position: absolute; left: 592px; top: 104px; width: 442px; height: 290px;
    border: 3px solid var(--screen-frame);
    background: radial-gradient(ellipse at 50% 70%, var(--screen-glow) 0%, #a9a567 40%, var(--screen-olive) 75%, #6e7a3c 100%);
    box-shadow: 0 4px 14px rgba(0,0,0,0.25);
  }
  .presenter {
    position: absolute; left: 98px; top: 76px; width: 356px; height: 599px;
    border-radius: 140px 140px 0 0;
    background: linear-gradient(180deg, var(--presenter-tone) 0%, var(--presenter-tone) 62%, var(--presenter-dark) 70%, var(--presenter-dark) 100%);
  }

  .control-panel {
    position: absolute; left: 279px; top: 583px; width: 642px; height: 92px;
    background: var(--panel-bg);
    border-radius: 8px 8px 0 0;
    display: flex; align-items: flex-start; gap: 10px; padding: 14px 14px 0;
  }
  .control-tile {
    width: 68px; height: 68px; flex: none;
    background: var(--tile-teal);
    border: 2px solid var(--tile-border);
    display: flex; flex-direction: column; align-items: center;
    padding-top: 5px;
  }
  .control-icon {
    width: 38px; height: 38px; border-radius: 50%;
    background: var(--icon-disc);
    display: flex; align-items: center; justify-content: center;
  }
  .control-icon svg { width: 24px; height: 24px; }
  .control-label {
    margin-top: 7px;
    font-size: 8.5px; line-height: 1; color: var(--label);
    text-transform: uppercase; white-space: nowrap; letter-spacing: -0.1px;
  }

  .panel-divider {
    width: 1px; height: 60px; margin: 4px 2px 0;
    background: rgba(255, 255, 255, 0.35); flex: none;
  }
  .status-indicator {
    width: 68px; height: 68px; flex: none;
    display: flex; flex-direction: column; align-items: center;
    padding-top: 5px;
  }
  .status-gauge {
    width: 38px; height: 38px;
    display: flex; align-items: center; justify-content: center;
  }
  .status-gauge svg { width: 38px; height: 38px; }
  .status-label {
    margin-top: 7px;
    font-size: 8.5px; line-height: 1; color: var(--meter-fill);
    text-transform: uppercase; white-space: nowrap; letter-spacing: -0.1px;
  }

  .step-nav {
    position: absolute; right: 4px; top: 650px;
    display: flex; gap: 5px;
  }
  .step-button {
    height: 21px; padding: 0 7px;
    background: var(--nav-bg); color: #fff;
    border: 1px solid #555; border-radius: 3px;
    font-size: 11px; font-weight: 700; line-height: 19px;
  }
</style>
</head>
<body>
  <div class="studio-backdrop" role="img" aria-label="Virtual news studio backdrop with curved sage walls and warm floor"></div>
  <div class="world-screen" role="img" aria-label="Wall screen showing a dotted world map on a glowing olive background"></div>
  <div class="presenter" role="img" aria-label="Smiling presenter in a blue shirt holding an open folder and pen"></div>

  <nav class="control-panel" aria-label="Simulation controls">
    <div class="control-tile">
      <span class="control-icon"><svg viewBox="0 0 24 24" fill="none" stroke="#1f5e56" stroke-width="1.8"><circle cx="12" cy="12" r="9"/><path d="M3 12h18M12 3c3 3 3 15 0 18M12 3c-3 3-3 15 0 18"/></svg></span>
      <span class="control-label">Map</span>
    </div>
    <div class="control-tile">
      <span class="control-icon"><svg viewBox="0 0 24 24" fill="#1f5e56"><path d="M7 3h10v18l-5-4-5 4z"/></svg></span>
      <span class="control-label">Bookmarks</span>
    </div>
    <div class="control-tile">
      <span class="control-icon"><svg viewBox="0 0 24 24" fill="none" stroke="#1f5e56" stroke-width="1.8"><path d="M6 3h9l4 4v14H6z"/><circle cx="11" cy="14" r="3"/><path d="M13 16l3 3"/></svg></span>
      <span class="control-label">Case Profile</span>
    </div>
    <div class="control-tile">
      <span class="control-icon"><svg viewBox="0 0 24 24" fill="#1f5e56"><path d="M6 3h9l4 4v14H6z"/></svg></span>
      <span class="control-label">Notes</span>
    </div>
    <div class="control-tile">
      <span class="control-icon"><svg viewBox="0 0 24 24" fill="none" stroke="#1f5e56" stroke-width="1.8"><rect x="3" y="6" width="18" height="12" rx="1"/><path d="M3 7l9 6 9-6"/></svg></span>
      <span class="control-label">Email</span>
    </div>
    <div class="control-tile">
      <span class="control-icon"><svg viewBox="0 0 24 24" fill="none" stroke="#1f5e56" stroke-width="1.8"><path d="M3 10c0-3 3-5 6-5s6 2 6 5-3 5-6 5l-3 2v-3c-2-1-3-2-3-4z"/><path d="M16 9c3 0 5 2 5 4 0 1.5-1 2.5-2 3v3l-3-2c-2 0-3-1-4-2"/></svg></span>
      <span class="control-label">Chat</span>
    </div>

    <span class="panel-divider" aria-hidden="true"></span>

    <div class="status-indicator" role="status" aria-label="Success rate: two of three stars">
      <span class="status-gauge"><svg viewBox="0 0 38 38">
        <circle cx="19" cy="19" r="17" fill="none" stroke="var(--meter-track)" stroke-width="2"/>
        <path d="M9 15l1.4 2.9 3.2.4-2.3 2.2.6 3.1L9 22.1l-2.9 1.5.6-3.1-2.3-2.2 3.2-.4z" fill="var(--star-gold)"/>
        <path d="M19 15l1.4 2.9 3.2.4-2.3 2.2.6 3.1-2.9-1.5-2.9 1.5.6-3.1-2.3-2.2 3.2-.4z" fill="var(--star-gold)"/>
        <path d="M29 15l1.4 2.9 3.2.4-2.3 2.2.6 3.1-2.9-1.5-2.9 1.5.6-3.1-2.3-2.2 3.2-.4z" fill="none" stroke="var(--star-gold)" stroke-width="1"/>
      </svg></span>
      <span class="status-label">Success Rate</span>
    </div>
    <div class="status-indicator" role="status" aria-label="Progress: about two thirds complete">
      <span class="status-gauge"><svg viewBox="0 0 38 38">
        <circle cx="19" cy="19" r="15" fill="none" stroke="var(--meter-track)" stroke-width="4"/>
        <circle cx="19" cy="19" r="15" fill="none" stroke="var(--meter-fill)" stroke-width="4" stroke-linecap="round" stroke-dasharray="63 95" transform="rotate(-90 19 19)"/>
        <circle cx="19" cy="19" r="3" fill="var(--meter-fill)"/>
      </svg></span>
      <span class="status-label">Progress</span>
    </div>
  </nav>

  <div class="step-nav">
    <span class="step-button">&lt; PREV</span>
    <span class="step-button">NEXT &gt;</span>
  </div>
</body>
</html>
```